Create a Fresh, Fun Design for Fruit and Veg Delivery Box

We’re Grow Some Sunshine, a fruit and vegetable delivery service that brings fresh produce to your doorstep. We're looking for a creative designer to create the look of our new packaging!

Design Details:

Box colour: Light brown cardboard
Colour scheme: One colour (your choice!)
Website: growsomesunshine.com.au
Images attached with dimensions and rough design ideas for inspiration.
Logo: It is preferred that the logo be included but not essential.

Target Market(s)

Families with young children.

Industry/Entity Type

Fruit and vegetable retail

Requirements
Should not have
• Do not use rainbows.

```html
<!DOCTYPE html>
<html lang="en">
<head>
<meta charset="utf-8">
<title>Grow Some Sunshine – Delivery Box Panels</title>
<link href="https://fonts.googleapis.com/css2?family=Bebas+Neue&family=Barlow+Condensed:wght@600;700&display=swap" rel="stylesheet">
<style>
  :root {
    --kraft: #c0a584;
    --kraft-light: #ccb290;
    --kraft-tint: #a9a47a;
    --green: #0b7a43;
    --green-deep: #0a6f3c;
    --green-tint: #3e8f5c;
    --paper: #ffffff;
    --handle: #ffffff;
  }
  * { margin: 0; padding: 0; box-sizing: border-box; }
  html, body { width: 900px; height: 1200px; overflow: hidden; background: var(--paper); }
  .canvas { position: relative; width: 900px; height: 1200px; }

  .panel { position: absolute; overflow: hidden; background: var(--kraft); }
  .panel--long { left: 60px; width: 780px; height: 316px; }
  .panel--brand { top: 50px; }
  .panel--message { top: 406px; }
  .panel--end { top: 762px; width: 370px; height: 270px; }
  .panel--end-left { left: 60px; }
  .panel--end-right { left: 470px; }

  .produce-pattern { position: absolute; left: 0; width: 100%; }
  .produce-pattern--kraft {
    top: 0; height: 49.5%;
    background:
      radial-gradient(ellipse 22% 60% at 12% 45%, var(--kraft-tint), transparent 70%),
      radial-gradient(ellipse 22% 60% at 38% 55%, var(--kraft-tint), transparent 70%),
      radial-gradient(ellipse 22% 60% at 62% 45%, var(--kraft-tint), transparent 70%),
      radial-gradient(ellipse 22% 60% at 88% 55%, var(--kraft-tint), transparent 70%),
      linear-gradient(180deg, var(--kraft-light), var(--kraft));
  }
  .produce-pattern--green {
    bottom: 0; height: 50.5%;
    background:
      radial-gradient(ellipse 30% 55% at 18% 50%, var(--green-tint), transparent 72%),
      radial-gradient(ellipse 30% 55% at 50% 60%, var(--green-tint), transparent 72%),
      radial-gradient(ellipse 30% 55% at 82% 45%, var(--green-tint), transparent 72%),
      linear-gradient(180deg, var(--green), var(--green-deep));
  }

  .brand-band {
    position: absolute; left: 0; bottom: 0; width: 100%; height: 50.5%;
    background: var(--green);
    display: flex; align-items: center; justify-content: center;
  }
  .brand-name {
    font-family: "Bebas Neue", sans-serif;
    color: var(--kraft);
    font-size: 78px; line-height: 1; text-align: center;
    letter-spacing: 1px; padding-top: 6px;
  }

  .message {
    position: absolute; inset: 0;
    display: flex; flex-direction: column; align-items: center; justify-content: center;
    color: var(--green); text-align: center;
  }
  .message__headline {
    font-family: "Bebas Neue", sans-serif; font-weight: 400;
    font-size: 60px; line-height: 0.97; letter-spacing: 1px;
  }
  .message__cta {
    font-family: "Barlow Condensed", sans-serif; font-weight: 600;
    font-size: 23px; margin-top: 14px; letter-spacing: 0.3px;
  }
  .message__url {
    font-family: "Barlow Condensed", sans-serif; font-weight: 700;
    font-size: 21px; margin-top: 6px;
    background: var(--green); color: var(--kraft);
    padding: 2px 22px 3px; border-radius: 18px; letter-spacing: 0.4px;
  }

  .end-label {
    position: absolute; left: 0; top: 0; width: 100%; height: 49.5%;
    display: flex; justify-content: center; text-align: center;
    color: var(--green);
  }
  .end-label--slogan {
    font-family: "Bebas Neue", sans-serif;
    font-size: 50px; line-height: 0.9; letter-spacing: 1px;
    align-items: flex-start; padding-top: 26px;
  }
  .end-label--url {
    font-family: "Barlow Condensed", sans-serif; font-weight: 700;
    font-size: 28px; align-items: flex-start; padding-top: 60px;
  }
  .hand-hole {
    position: absolute; left: 50%; top: 138px;
    width: 130px; height: 36px; margin-left: -65px;
    background: var(--handle); border-radius: 18px;
  }
</style>
</head>
<body>
<main class="canvas">

  <section class="panel panel--long panel--brand">
    <div class="produce-pattern produce-pattern--kraft" role="img" aria-label="Green line-drawn pattern of vegetables: ginger, chillies, olives, carrots, tomatoes, capsicum, broccoli and eggplant"></div>
    <div class="brand-band">
      <p class="brand-name">Grow Some Sunshine</p>
    </div>
  </section>

  <section class="panel panel--long panel--message">
    <div class="message">
      <h1 class="message__headline">Fresh Farm Produce<br>Straight to Your Doorstep!</h1>
      <p class="message__cta">PLACE YOUR ORDER</p>
      <p class="message__url">www.growsomesunshine.com.au</p>
    </div>
  </section>

  <section class="panel panel--end panel--end-left">
    <p class="end-label end-label--slogan">Freshness<br>Guaranteed!</p>
    <div class="produce-pattern produce-pattern--green" role="img" aria-label="Kraft line-drawn vegetable pattern on green: carrots, ginger, chilli, olives, tomato, capsicum, broccoli and eggplant"></div>
    <div class="hand-hole"></div>
  </section>

  <section class="panel panel--end panel--end-right">
    <p class="end-label end-label--url">growsomesunshine.com.au</p>
    <div class="produce-pattern produce-pattern--green" role="img" aria-label="Kraft line-drawn vegetable pattern on green: capsicum, leek, pumpkin, carrot, ginger, mushrooms and olives"></div>
    <div class="hand-hole"></div>
  </section>

</main>
</body>
</html>
```